依頼詳細
【必ず入れて頂きたい要素】
①「アルコールと天然由来成分のチカラで室内除菌」というキャッチコピー。
②画像を使用し、キャッチコピーのイメージを入居者様が勝手に抱くデザイン。
※キャッチコピーとデザインで勝負し、下記の補足説明は可能な限り文字数を少なく、小さくする。

【補足説明として入れて頂きたい要素】
①「消臭・除菌施工サービス」というサービス名称。
②アルコールと国産の天然ひのきと緑茶エキスを使用。
③「中和反応法で悪臭の原因成分を分解」という事を添付画像「中和反応法」
のように図で説明。
④「第三者機関で効果を検証」という文言。
※添付画像「室内空気衛生推進連盟」のマークを挿入。

⑤2つの会社情報を記入するスペースを確保
1つは自由に社名や電話番号を記載できるように空欄とする
スペースのタイトルは「サービス提供会社」

1つは弊社の下記情報を記載
タイトルは「技術提供会社」
添付画像「会社ロゴ」
住所:東京都港区芝浦4-17-6森田ビル5F
電話:03-5871-2943
Mail:info@kt-planwork.jp
記載項目
株式会社住環境企画工房/東京都港区芝浦4-17-6森田ビル5F
電話:03-5871-2943/Mail:info@kt-planwork.jp
サイズ
A4
ページ数
片面
希望イメージ
シンプル 複雑
単色 カラフル
暗い 明るい
日常 高級
遊び心 厳粛
未来的 伝統的
女性的 男性的
希望する色
緑系、青系、水色系
納品ファイル
• 高解像度JPG (.jpg)
• イラストレーター形式 (.ai)
• PNG形式 (.png)
補足説明
下記3種のファイルでの納品お願い致します。
Ai(アウトライン前とアウトライン後)
PDF
jpg
(全てトンボ有り・無し両方)

```html
<!DOCTYPE html>
<html lang="ja">
<head>
<meta charset="utf-8">
<title>室内除菌 消臭・除菌施工サービス</title>
<link rel="stylesheet" href="https://fonts.googleapis.com/css2?family=Noto+Sans+JP:wght@400;500;700;900&display=swap">
<style>
  :root {
    --teal: #1597b4;
    --teal-deep: #0d7c98;
    --sky: #d9eef8;
    --sky-pale: #eef7fc;
    --green: #4da12f;
    --green-pale: #d7eccb;
    --ink: #333d44;
    --grey: #8a9297;
    --line: #b9c3c8;
    --white: #ffffff;
  }
  * { margin: 0; padding: 0; box-sizing: border-box; }
  html, body { width: 849px; height: 1200px; overflow: hidden; background: var(--white); }
  body { font-family: "Noto Sans JP", sans-serif; color: var(--ink); }
  .poster { position: relative; width: 849px; height: 1200px; overflow: hidden; background: var(--white); }

  .hero-photo {
    position: absolute; left: 0; top: 0; width: 849px; height: 720px;
    background: linear-gradient(160deg, #f7fafb 0%, #e9eff1 45%, #dfe6e4 70%, #f3f6f5 100%);
  }
  .hero-fade {
    position: absolute; left: 0; top: 560px; width: 849px; height: 160px;
    background: linear-gradient(180deg, rgba(255,255,255,0) 0%, var(--sky-pale) 100%);
  }

  .catch { position: absolute; left: 0; top: 0; width: 849px; height: 500px; }
  .catch span { position: absolute; font-weight: 900; white-space: nowrap; line-height: 1;
    -webkit-text-stroke: 8px var(--white); paint-order: stroke fill; }
  .catch .c1 { left: 283px; top: 64px; font-size: 54px; color: var(--teal); }
  .catch .c2 { left: 262px; top: 140px; font-size: 48px; color: var(--teal); }
  .catch .c2b { left: 566px; top: 160px; font-size: 28px; color: var(--ink); }
  .catch .c3 { left: 300px; top: 218px; font-size: 122px; letter-spacing: 4px; color: var(--teal-deep); }
  .catch .c4 { left: 300px; top: 350px; font-size: 122px; letter-spacing: 4px; color: var(--teal-deep); }

  .service-band {
    position: absolute; left: 0; top: 680px; width: 849px; height: 255px;
    background: linear-gradient(180deg, var(--sky-pale) 0%, var(--sky) 60%, #cfe8f4 100%);
  }
  .service-name { position: absolute; left: 28px; top: 730px; }
  .service-name .lead { display: block; font-size: 44px; font-weight: 900; color: var(--green); line-height: 1.15; letter-spacing: 1px; }
  .service-name .sub { display: block; font-size: 36px; font-weight: 700; color: var(--ink); line-height: 1.25; letter-spacing: 1px; }

  .ingredients { position: absolute; left: 440px; top: 700px; }

  .reaction { position: absolute; left: 450px; top: 848px; }
  .reaction .title { font-size: 16px; font-weight: 700; color: var(--green); }
  .reaction .note { font-size: 11px; color: var(--grey); margin-top: 1px; }
  .reaction-diagram { position: absolute; left: 615px; top: 838px; }

  .contact-head { position: absolute; left: 14px; top: 942px; font-size: 14px; color: var(--grey); }
  .contact-row { position: absolute; left: 14px; top: 966px; width: 821px; height: 208px; display: flex; gap: 8px; }
  .provider-box { width: 496px; border: 1.5px solid var(--line); padding: 10px 14px; }
  .provider-box .box-title { font-size: 12px; color: var(--grey); }
  .tech-tag { width: 34px; border: 1.5px solid var(--line); writing-mode: vertical-rl; font-size: 13px;
    color: var(--grey); display: flex; align-items: center; justify-content: center; letter-spacing: 3px; }
  .tech-info { width: 214px; padding: 8px 2px; font-size: 11.5px; line-height: 1.7; }
  .tech-info .brand { display: flex; align-items: center; gap: 6px; font-size: 14px; font-weight: 700; color: var(--teal-deep); margin-bottom: 6px; white-space: nowrap; }
  .tech-info .brand i { display: block; width: 14px; height: 14px; background: var(--teal-deep); flex: none; }
  .cert { width: 53px; display: flex; flex-direction: column; align-items: center; gap: 6px; padding-top: 4px; }
  .cert .cert-name { writing-mode: vertical-rl; font-size: 10.5px; line-height: 1; height: 118px; letter-spacing: 0.5px; color: var(--ink); white-space: nowrap; }
  .cert .cert-mark { width: 44px; height: 44px; border-radius: 50%; border: 3px solid var(--green); background: var(--green-pale); flex: none; }
  .cert .verified { font-size: 8.5px; color: var(--grey); text-align: center; line-height: 1.3; white-space: nowrap; }
</style>
</head>
<body>
<div class="poster">
  <div class="hero-photo" role="img" aria-label="明るいリビングで両腕を上げて伸びをする女性、白い家具と観葉植物のある清潔な室内の写真"></div>
  <div class="hero-fade"></div>

  <h1 class="catch">
    <span class="c1">アルコールと</span>
    <span class="c2">天然由来成分</span>
    <span class="c2b">のチカラで</span>
    <span class="c3">室内</span>
    <span class="c4">除菌</span>
  </h1>

  <div class="service-band"></div>

  <h2 class="service-name">
    <span class="lead">消臭・除菌</span>
    <span class="sub">施工サービス</span>
  </h2>

  <svg class="ingredients" width="400" height="140" viewBox="0 0 400 140">
    <defs>
      <radialGradient id="alcoholFill" cx="50%" cy="40%" r="60%">
        <stop offset="0%" stop-color="#ffffff"/>
        <stop offset="100%" stop-color="#c7e6f3"/>
      </radialGradient>
      <radialGradient id="hinokiFill" cx="50%" cy="45%" r="60%">
        <stop offset="0%" stop-color="#8fc46a"/>
        <stop offset="100%" stop-color="#3d7f2a"/>
      </radialGradient>
      <radialGradient id="teaFill" cx="50%" cy="45%" r="60%">
        <stop offset="0%" stop-color="#c9e6a8"/>
        <stop offset="100%" stop-color="#6ea945"/>
      </radialGradient>
    </defs>
    <circle cx="68" cy="70" r="62" fill="url(#alcoholFill)" stroke="#ffffff" stroke-width="5"/>
    <circle cx="50" cy="38" r="7" fill="none" stroke="#8ccbe3" stroke-width="2"/>
    <circle cx="92" cy="104" r="5" fill="none" stroke="#8ccbe3" stroke-width="2"/>
    <circle cx="100" cy="44" r="4" fill="none" stroke="#8ccbe3" stroke-width="2"/>
    <g role="img" aria-label="天然ひのきの枝葉の写真">
      <circle cx="198" cy="70" r="62" fill="url(#hinokiFill)" stroke="#ffffff" stroke-width="5"/>
    </g>
    <g role="img" aria-label="緑茶の葉の写真">
      <circle cx="328" cy="70" r="62" fill="url(#teaFill)" stroke="#ffffff" stroke-width="5"/>
    </g>
    <rect x="22" y="58" width="92" height="26" rx="13" fill="#1597b4"/>
    <rect x="152" y="58" width="92" height="26" rx="13" fill="#4da12f"/>
    <rect x="282" y="58" width="92" height="26" rx="13" fill="#4da12f"/>
    <g font-family="Noto Sans JP, sans-serif" font-size="14" font-weight="700" fill="#ffffff" text-anchor="middle">
      <text x="68" y="76">アルコール</text>
      <text x="198" y="76">天然ひのき</text>
      <text x="328" y="76">緑茶エキス</text>
    </g>
    <circle cx="133" cy="70" r="13" fill="#4da12f" stroke="#ffffff" stroke-width="2"/>
    <circle cx="263" cy="70" r="13" fill="#4da12f" stroke="#ffffff" stroke-width="2"/>
    <g stroke="#ffffff" stroke-width="3.5" stroke-linecap="round">
      <line x1="127" y1="70" x2="139" y2="70"/><line x1="133" y1="64" x2="133" y2="76"/>
      <line x1="257" y1="70" x2="269" y2="70"/><line x1="263" y1="64" x2="263" y2="76"/>
    </g>
  </svg>

  <div class="reaction">
    <p class="title">悪臭の原因成分を分解</p>
    <p class="note">（中和反応法）</p>
  </div>

  <svg class="reaction-diagram" width="220" height="70" viewBox="0 0 220 70">
    <circle cx="22" cy="30" r="17" fill="#d7eccb" stroke="#4da12f" stroke-width="2"/>
    <text x="22" y="62" font-size="9" fill="#8a9297" text-anchor="middle" font-family="Noto Sans JP, sans-serif">除菌成分</text>
    <text x="56" y="35" font-size="16" fill="#8a9297" text-anchor="middle" font-family="Noto Sans JP, sans-serif">＋</text>
    <circle cx="90" cy="30" r="13" fill="#e3d5b8"/>
    <text x="90" y="62" font-size="9" fill="#8a9297" text-anchor="middle" font-family="Noto Sans JP, sans-serif">臭い</text>
    <line x1="114" y1="30" x2="150" y2="30" stroke="#8a9297" stroke-width="2"/>
    <polygon points="150,24 160,30 150,36" fill="#8a9297"/>
    <circle cx="190" cy="30" r="21" fill="#ffffff" stroke="#4da12f" stroke-width="3"/>
  </svg>

  <p class="contact-head">問い合わせ先</p>
  <div class="contact-row">
    <div class="provider-box"><p class="box-title">サービス提供会社</p></div>
    <div class="tech-tag">技術提供会社</div>
    <div class="tech-info">
      <p class="brand"><i></i>株式会社住環境企画工房</p>
      <p>東京都港区芝浦4-17-6森田ビル5F</p>
      <p>電話：03-5871-2943</p>
      <p>Mail：info@kt-planwork.jp</p>
    </div>
    <div class="cert">
      <p class="cert-name">室内空気衛生推進連盟</p>
      <div class="cert-mark"></div>
      <p class="verified">第三者機関で<br>効果を検証</p>
    </div>
  </div>
</div>
</body>
</html>
```